We are a all around maintence company for outdoor services. Commercial and residential: mowing, sprinkler repairs, power washing, parking lot striping, tree trimming, gutters cleaning, pond cleaning,feeding and fertilizing, flower bed clean up and fence repair.

Industry/Entity Type

It Company

Contact Information for Business Card

Bramblewick Yard Services
R.K. Mondavel
Cell 555-318-6047
P.O. Box 4518
Amarillo,Tx 00000
Office 555-294-7730
Fax 555-294-7738

```html
<!DOCTYPE html>
<html lang="en">
<head>
<meta charset="utf-8">
<title>Bramblewick Yard Services – Business Card</title>
<link rel="stylesheet" href="https://fonts.googleapis.com/css2?family=Archivo+Black&family=Roboto:wght@300;400;700&display=swap">
<style>
  :root {
    --band-blue: #34529a;
    --leaf-green: #119a4b;
    --ink: #111111;
    --text-grey: #1a1a1a;
    --muted: #444444;
    --paper: #ffffff;
    --icon-tint: #6f86bd;
  }
  * { margin: 0; padding: 0; box-sizing: border-box; }
  html, body {
    width: 1200px;
    height: 702px;
    overflow: hidden;
    background: var(--paper);
  }
  .card {
    position: relative;
    width: 1200px;
    height: 702px;
    background: var(--paper);
  }
  .brand-band {
    position: absolute;
    left: 0; top: 0;
    width: 383px;
    height: 702px;
    background: var(--band-blue);
  }
  .brand-mark {
    position: absolute;
    left: 119px; top: 69px;
    width: 216px; height: 216px;
  }
  .brand-name {
    position: absolute;
    left: 119px; top: 153px;
    width: 216px;
    text-align: center;
    font-family: "Roboto", sans-serif;
    font-weight: 700;
    font-size: 21px;
    line-height: 1.25;
    color: var(--band-blue);
  }
  .tool-icons {
    position: absolute;
    left: 166px; top: 292px;
    width: 100px; height: 346px;
    border-radius: 8px;
    background: linear-gradient(180deg, var(--icon-tint), #5a73b0);
  }
  .offer {
    position: absolute;
    left: 383px; top: 0;
    width: 817px;
    height: 702px;
    text-align: center;
  }
  .company-title {
    position: absolute;
    left: 0; top: 140px;
    width: 100%;
    font-family: "Archivo Black", sans-serif;
    font-weight: 400;
    font-size: 46px;
    line-height: 1;
    color: var(--ink);
  }
  .service-list {
    position: absolute;
    left: 0; top: 290px;
    width: 100%;
    list-style: none;
    font-family: "Roboto", sans-serif;
    font-weight: 300;
    font-size: 39px;
    color: var(--text-grey);
  }
  .service-row {
    height: 55.4px;
    line-height: 48px;
    white-space: nowrap;
  }
  .service {
    display: inline-flex;
    align-items: center;
  }
  .service + .service { margin-left: 12px; }
  .service::before {
    content: "";
    width: 15px; height: 15px;
    border-radius: 50%;
    background: var(--leaf-green);
    margin-right: 8px;
  }
  .contact {
    position: absolute;
    left: 0; top: 598px;
    width: 100%;
    font-family: "Roboto", sans-serif;
    font-weight: 400;
    font-size: 18px;
    line-height: 28px;
    color: var(--muted);
    font-style: normal;
  }
  .contact-name {
    font-weight: 700;
    color: var(--ink);
  }
  .contact-sep {
    display: inline-block;
    width: 7px; height: 7px;
    border-radius: 50%;
    background: var(--leaf-green);
    margin: 0 10px;
    vertical-align: middle;
  }
</style>
</head>
<body>
<div class="card">
  <aside class="brand-band">
    <svg class="brand-mark" viewBox="0 0 216 216" aria-hidden="true">
      <circle cx="108" cy="108" r="108" fill="#ffffff"/>
    </svg>
    <p class="brand-name">Bramblewick<br>Yard Services</p>
    <div class="tool-icons" role="img" aria-label="Column of white tool icons: lawn mower, pruning shears, sprinkler and crossed rake and shovel"></div>
  </aside>

  <section class="offer">
    <h1 class="company-title">Bramblewick Yard Services</h1>
    <ul class="service-list">
      <li class="service-row"><span class="service">mowing</span><span class="service">sprinkler repairs</span></li>
      <li class="service-row"><span class="service">power washing</span><span class="service">parking lot striping</span></li>
      <li class="service-row"><span class="service">tree trimming</span><span class="service">gutters cleaning</span></li>
      <li class="service-row"><span class="service">pond cleaning</span><span class="service">feeding and fertilizing</span></li>
      <li class="service-row"><span class="service">flower bed clean</span><span class="service">fence repair</span></li>
    </ul>
    <address class="contact">
      <span class="contact-name">R.K. Mondavel</span><span class="contact-sep"></span>Cell 555-318-6047<span class="contact-sep"></span>P.O. Box 4518, Amarillo, TX 00000<br>
      Office 555-294-7730<span class="contact-sep"></span>Fax 555-294-7738
    </address>
  </section>
</div>
</body>
</html>
```